Hollowmere Farm Promotional Leaflet

The team at Hollowmere Farm can help with every aspect of managing and enhancing your home from housekeeping and professional cleaning, laundry and ironing to providing chic and contemporary flower arrangements and even food for your pets!We take pride in providing high-end, consistent and reliable professional services bespoke to you. Whether you are a busy professional working long hours, a stay-at home parent or retired; having professional help in the home gives you time to spend on the things you enjoy.We are providing a very upmarket, highly professional service and need an A5 promotional leaflet to be designed. Please refer to www.hollowmerefarm-example.co.uk and see the section on 'Home Management'The leaflet should incorporate the Hollowmere Farm logo without the 'tipi', and any suitable photography images used on the home page of the website or the 'home management' section.

Target Market(s)

high-end, affluent owners of luxury homes

Industry/Entity Type

Farm

Contact Information for Business Card

The business card design needs to be suitable for use across all of Hollowmere Farm businesses, specifically:
Hollowmere Farm Home Management - otherwise known as Hollowmere Farm @ Home (this uses the typographical logo
Hollowmere Farm Weddings & Events - this uses the 'tipi' logo

Requirements
Must have
• Design in keeping with the look and feel of the logo and website design
• www.hollowmerefarm-example.co.uk

```html
<!DOCTYPE html>
<html lang="en">
<head>
<meta charset="utf-8">
<title>Hollowmere Farm Business Card</title>
<link rel="stylesheet" href="https://fonts.googleapis.com/css2?family=Roboto:wght@400;500;700&display=swap">
<style>
  :root {
    --stage: #e9e6e1;
    --card-white: #ffffff;
    --card-dark: #221f20;
    --pattern-tone: #2b2426;
    --brand-pink: #dc1f5e;
    --brand-gold: #e8c06a;
    --ink: #4a4a4a;
    --muted: #8a8585;
  }
  * { box-sizing: border-box; margin: 0; padding: 0; }
  html, body { width: 1200px; height: 911px; overflow: hidden; }
  body {
    background: var(--stage);
    font-family: "Roboto", Arial, sans-serif;
    position: relative;
  }
  .card {
    position: absolute;
    left: 320px;
    width: 560px;
    height: 320px;
    border-radius: 18px;
    overflow: hidden;
    box-shadow: 0 6px 18px rgba(0,0,0,0.12);
  }
  .card--front { top: 100px; background: var(--card-white); }
  .card--back { top: 490px; background: var(--card-dark); }

  .name-band {
    position: absolute;
    left: 0; top: 148px;
    width: 262px; height: 66px;
    background: var(--brand-pink);
    padding: 12px 0 0 26px;
  }
  .name-band__name {
    color: #fff; font-weight: 500; font-size: 19px; letter-spacing: 0.5px;
  }
  .name-band__role {
    color: var(--brand-gold); font-size: 13px; margin-top: 4px; letter-spacing: 0.3px;
  }
  .wordmark {
    position: absolute;
    color: var(--brand-pink);
    font-weight: 500;
    white-space: nowrap;
  }
  .card--front .wordmark { left: 282px; top: 160px; font-size: 30px; }
  .contact {
    position: absolute;
    left: 150px; top: 236px;
    color: var(--ink);
    font-size: 12.5px;
    line-height: 17px;
  }
  .contact__line { display: flex; align-items: center; gap: 6px; }
  .contact__line svg { width: 12px; height: 12px; flex: none; }
  .contact__line--plain { padding-left: 18px; }

  .pattern-fill {
    position: absolute; inset: 0;
    background: radial-gradient(ellipse at center, var(--pattern-tone), var(--card-dark) 75%);
  }
  .card--back .wordmark {
    left: 0; right: 0; top: 138px; text-align: center; font-size: 38px;
  }
  .back-url {
    position: absolute;
    left: 28px; top: 160px;
    transform-origin: left center;
    transform: rotate(90deg) translate(-130px, 0);
    color: var(--muted);
    font-size: 11px; letter-spacing: 2.5px;
    white-space: nowrap;
  }
</style>
</head>
<body>
  <section class="card card--front">
    <div class="name-band">
      <p class="name-band__name">ELLIS MARDEN</p>
      <p class="name-band__role">CEO/FOUNDER</p>
    </div>
    <p class="wordmark">Hollowmere Farm</p>
    <div class="contact">
      <p class="contact__line contact__line--plain">Hollowmere Farm</p>
      <p class="contact__line contact__line--plain">Mill Lane, Ashcombe</p>
      <p class="contact__line contact__line--plain">Wessex AB1 2CD, GB</p>
      <p class="contact__line">
        <svg viewBox="0 0 12 12" aria-hidden="true"><path d="M3 1 L5 3.5 L4 5 Q5 7 7 8 L8.5 7 L11 9 L9.5 11 Q4 10.5 1 3 Z" fill="var(--brand-pink)"/></svg>
        +44 7700 900412
      </p>
      <p class="contact__line">
        <svg viewBox="0 0 12 12" aria-hidden="true"><circle cx="6" cy="6" r="5.5" fill="var(--brand-pink)"/><circle cx="6" cy="6" r="3.2" fill="none" stroke="#fff" stroke-width="1"/><path d="M2.8 6 H9.2 M6 2.8 V9.2" stroke="#fff" stroke-width="0.8"/></svg>
        www.hollowmerefarm-example.co.uk
      </p>
    </div>
  </section>

  <section class="card card--back">
    <div class="pattern-fill" role="img" aria-label="Faint repeated brand name pattern across the dark card back"></div>
    <p class="back-url">www.hollowmerefarm-example.co.uk</p>
    <p class="wordmark">Hollowmere Farm</p>
  </section>
</body>
</html>
```